Simple-clean design for Brightora!!

We need a business card for consulting company. Our company is consulting industry, but not too "intelligent" or "noble". We are expecting something "simple-clean" or "friendly", but something colorful with 3 colors. Our customers would be from all over the world. Brightora stands for "wisdom" and "knowledge". We are supporting all companies who are trying to launch a business in Japan. We don't want to give an impression it is very hard or big barrier to dive into Japan market to start a business.

Target Market(s)

Companies all over the world!

Industry/Entity Type

Management Consulting

Contact Information for Business Card

Please refer to the attachments. Use those colors. Telephone, mail, URL could be friendly icons.

Requirements
Must have
• Name: Takeshi Minabe
• Title: Founder & CEO
• Mail: takeshi.minabe@brightora.co
• Web: www.brightora.co
• Address: Kozuenori Building 6th Floor
• 3-5-24, Hamazono Chuo-ku Tokyo
• 104-0193 JAPAN
Nice to have
• We are Japanese company so if you can design with Japanese fonts too, you will be ranked at very high place!!

```html
<!DOCTYPE html>
<html lang="en">
<head>
<meta charset="utf-8">
<title>Brightora Business Card</title>
<link href="https://fonts.googleapis.com/css2?family=Nunito:wght@400;600;700&display=swap" rel="stylesheet">
<style>
  :root {
    --page: #ecebe8;
    --card: #ffffff;
    --green: #8cc43f;
    --green-soft: #e6f1d6;
    --charcoal: #3a3a3c;
    --grey-soft: #dcdcdc;
    --ink: #5a5a5a;
    --white: #ffffff;
  }
  * { box-sizing: border-box; margin: 0; padding: 0; }
  html, body { width: 845px; height: 1200px; overflow: hidden; }
  body {
    background: var(--page);
    font-family: "Nunito", sans-serif;
    position: relative;
  }
  .card {
    position: absolute;
    left: 72px;
    width: 700px;
    height: 400px;
    background: var(--card);
    box-shadow: 0 6px 18px rgba(0,0,0,0.18);
    overflow: hidden;
  }
  .card--front { top: 120px; }
  .card--back { top: 680px; }
  .card__shapes { position: absolute; inset: 0; }

  /* Front */
  .front__brand {
    position: absolute;
    left: 330px; top: 82px;
    font-size: 46px; font-weight: 700;
    color: var(--white); letter-spacing: 1px;
  }
  .front__icons {
    position: absolute; left: 540px; top: 82px;
    display: flex; gap: 14px;
  }
  .icon-badge {
    width: 34px; height: 34px; border-radius: 50%;
    background: var(--white);
    display: flex; align-items: center; justify-content: center;
  }
  .icon-badge svg { width: 18px; height: 18px; }
  .front__mark {
    position: absolute; left: 80px; top: 200px;
    width: 110px; height: 110px; border-radius: 50%;
    background: var(--grey-soft);
  }
  .front__web {
    position: absolute; left: 300px; top: 282px;
    font-size: 20px; font-weight: 600; color: var(--ink);
    letter-spacing: 1px;
  }

  /* Back */
  .back__contact {
    position: absolute; left: 300px; top: 58px;
    color: var(--white);
  }
  .back__name { font-size: 22px; font-weight: 700; }
  .back__title { font-size: 13px; font-weight: 600; margin-bottom: 12px; }
  .back__list { list-style: none; font-size: 11.5px; line-height: 1.65; }
  .back__list li { display: flex; align-items: flex-start; gap: 8px; }
  .back__list svg { width: 12px; height: 12px; flex: none; margin-top: 3px; }
  .back__brand {
    position: absolute; left: 60px; top: 290px;
    display: flex; align-items: center; gap: 12px;
  }
  .back__dot { width: 40px; height: 40px; border-radius: 50%; background: var(--green); }
  .back__brand-name { font-size: 36px; font-weight: 700; color: var(--green); }
</style>
</head>
<body>

<section class="card card--front" aria-label="Card front">
  <svg class="card__shapes" viewBox="0 0 700 400" aria-hidden="true">
    <polygon points="300,40 700,40 700,190 660,200 260,200" fill="var(--green)"/>
    <polygon points="0,350 520,350 560,400 0,400" fill="var(--charcoal)"/>
  </svg>
  <div class="front__brand">brightora</div>
  <div class="front__icons">
    <span class="icon-badge" aria-label="Phone">
      <svg viewBox="0 0 24 24"><path d="M6.6 10.8a15 15 0 0 0 6.6 6.6l2.2-2.2c.3-.3.7-.4 1-.2 1.1.4 2.3.6 3.6.6.6 0 1 .4 1 1V20c0 .6-.4 1-1 1A17 17 0 0 1 3 4c0-.6.4-1 1-1h3.5c.6 0 1 .4 1 1 0 1.3.2 2.5.6 3.6.1.3 0 .7-.2 1z" fill="var(--green)"/></svg>
    </span>
    <span class="icon-badge" aria-label="Mail">
      <svg viewBox="0 0 24 24"><rect x="3" y="6" width="18" height="12" rx="1.5" fill="var(--green)"/><path d="M3.5 7l8.5 6 8.5-6" stroke="#fff" stroke-width="1.6" fill="none"/></svg>
    </span>
    <span class="icon-badge" aria-label="Web">
      <svg viewBox="0 0 24 24" fill="none" stroke="var(--green)" stroke-width="2"><circle cx="12" cy="12" r="9"/><path d="M3 12h18M12 3c3 3 3 15 0 18M12 3c-3 3-3 15 0 18"/></svg>
    </span>
  </div>
  <div class="front__mark"></div>
  <div class="front__web">www.brightora.co</div>
</section>

<section class="card card--back" aria-label="Card back">
  <svg class="card__shapes" viewBox="0 0 700 400" aria-hidden="true">
    <rect x="0" y="30" width="700" height="200" fill="var(--green)"/>
    <polygon points="640,230 700,230 700,400 560,400" fill="var(--charcoal)"/>
  </svg>
  <div class="back__contact">
    <div class="back__name">Takeshi Minabe</div>
    <div class="back__title">Founder &amp; CEO</div>
    <ul class="back__list">
      <li><svg viewBox="0 0 24 24"><rect x="3" y="6" width="18" height="12" rx="1.5" fill="#fff"/></svg>takeshi.minabe@brightora.co</li>
      <li><svg viewBox="0 0 24 24" fill="none" stroke="#fff" stroke-width="2.4"><circle cx="12" cy="12" r="9"/><path d="M3 12h18"/></svg>www.brightora.co</li>
      <li><svg viewBox="0 0 24 24"><path d="M12 2a7 7 0 0 0-7 7c0 5 7 13 7 13s7-8 7-13a7 7 0 0 0-7-7z" fill="#fff"/></svg>
        <span>Kozuenori Building 6th Floor<br>3-5-24, Hamazono Chuo-ku Tokyo<br>104-0193 JAPAN</span></li>
    </ul>
  </div>
  <div class="back__brand">
    <span class="back__dot"></span>
    <span class="back__brand-name">brightora</span>
  </div>
</section>

</body>
</html>
```